Business Card and Word .doc header and footer required

I need a business card designed for my cybersecurity consulting company. Also required, is a header and footer to be ued for my word documents.
Attached is the Logo design, font and rgb used.

Industry/Entity Type

Cyber Security Consulting

Contact Information for Business Card

Name, Phone, email, website

Colors
0054AA
0677BA
7BADD7
CADEEF
E8F1F8

Requirements
Must have
• Sleek, modern

```html
<!DOCTYPE html>
<html lang="en">
<head>
<meta charset="utf-8">
<title>Northgate – Business Card</title>
<link rel="stylesheet" href="https://fonts.googleapis.com/css2?family=Poppins:wght@400;500;600&display=swap">
<style>
  :root {
    --brand-blue: #1b7aad;
    --brand-blue-deep: #0677ba;
    --card-bg: #efefef;
    --page-bg: #ffffff;
    --ink-dark: #2b2b2b;
    --ink-grey: #6a6a6a;
    --white: #ffffff;
  }
  * { box-sizing: border-box; margin: 0; padding: 0; }
  html, body { width: 1004px; height: 1200px; overflow: hidden; background: var(--page-bg); }
  body { font-family: "Poppins", sans-serif; position: relative; }

  .card {
    position: absolute;
    left: 62px;
    width: 880px;
    height: 528px;
    background: var(--card-bg);
    overflow: hidden;
  }
  .card--front { top: 48px; }
  .card--back  { top: 624px; }

  .brand-mark { width: 110px; height: 110px; border-radius: 50%; flex: none; }
  .brand-name { font-weight: 600; font-size: 36px; line-height: 36px; white-space: nowrap; }
  .brand-tagline {
    margin-top: 11px;
    font-size: 11px; line-height: 12px; font-weight: 500;
    letter-spacing: 2.6px; text-transform: uppercase; white-space: nowrap;
  }

  /* Front */
  .brand-panel {
    position: absolute;
    left: 98px; top: 0;
    width: 293px; height: 411px;
    background: var(--brand-blue);
    border-radius: 0 0 9px 9px;
    display: flex; flex-direction: column; align-items: center;
    padding-top: 113px;
  }
  .brand-panel .brand-mark { background: var(--white); }
  .brand-panel .brand-name { margin-top: 50px; color: var(--white); }
  .brand-panel .brand-tagline { color: var(--white); }

  .person { position: absolute; left: 525px; top: 114px; }
  .person__name {
    font-size: 30px; font-weight: 600; line-height: 32px;
    color: var(--brand-blue); letter-spacing: 0.5px; white-space: nowrap;
  }
  .person__name-last { font-weight: 400; color: var(--ink-dark); }
  .person__role {
    margin-top: 2px; font-size: 18px; line-height: 22px;
    color: var(--brand-blue-deep);
  }
  .person__rule {
    position: absolute; left: 691px; top: 159px;
    width: 189px; height: 2px; background: var(--ink-dark);
  }

  .address {
    position: absolute; left: 525px; top: 227px;
    font-size: 19px; line-height: 24px; color: var(--ink-grey);
  }
  .address__rule {
    position: absolute; left: 525px; top: 282px;
    width: 96px; height: 2px; background: var(--ink-dark);
  }

  .contact-list { position: absolute; left: 525px; top: 296px; list-style: none; }
  .contact-item {
    display: flex; align-items: center; height: 32px; margin-bottom: 8px;
    font-size: 19px; color: var(--ink-grey); letter-spacing: 0.3px; white-space: nowrap;
  }
  .contact-icon { width: 32px; height: 32px; margin-right: 17px; flex: none; }

  /* Back */
  .edge-tab {
    position: absolute; top: 118px; width: 59px; height: 292px;
    background: var(--brand-blue);
  }
  .edge-tab--left  { left: 0;  border-radius: 0 8px 8px 0; }
  .edge-tab--right { right: 0; border-radius: 8px 0 0 8px; }

  .back-brand {
    position: absolute; left: 0; right: 0; top: 133px;
    display: flex; flex-direction: column; align-items: center;
  }
  .back-brand .brand-mark { background: var(--brand-blue); }
  .back-brand .brand-name { color: var(--brand-blue); margin-top: 49px; }
  .back-brand .brand-tagline { color: var(--ink-dark); }

  .back-email {
    position: absolute; left: 0; right: 0; top: 437px;
    text-align: center; font-size: 16px; line-height: 22px; font-weight: 500;
    color: var(--ink-dark); letter-spacing: 0.3px;
  }
</style>
</head>
<body>

<section class="card card--front" aria-label="Business card front">
  <div class="brand-panel">
    <div class="brand-mark"></div>
    <div class="brand-name">Northgate</div>
    <div class="brand-tagline">Consulting Company</div>
  </div>

  <div class="person">
    <h1 class="person__name">ARLEN <span class="person__name-last">VOSS</span></h1>
    <p class="person__role">Graphic Designer</p>
  </div>
  <div class="person__rule"></div>

  <p class="address">210 Harbor Lane, Suite 4<br>Eastfield, NY 10012</p>
  <div class="address__rule"></div>

  <ul class="contact-list">
    <li class="contact-item">
      <svg class="contact-icon" viewBox="0 0 32 32" aria-hidden="true">
        <circle cx="16" cy="16" r="16" fill="#1b7aad"/>
        <path d="M9 14c0-3 3-5 7-5s7 2 7 5h-4v-2h-6v2z M10 15h12v7H10z" fill="#fff"/>
        <circle cx="16" cy="18.5" r="2" fill="#1b7aad"/>
      </svg>
      555 . 014 22907316
    </li>
    <li class="contact-item">
      <svg class="contact-icon" viewBox="0 0 32 32" aria-hidden="true">
        <circle cx="16" cy="16" r="16" fill="#1b7aad"/>
        <rect x="9" y="11" width="14" height="10" fill="none" stroke="#fff" stroke-width="1.6"/>
        <path d="M9 11l7 6 7-6" fill="none" stroke="#fff" stroke-width="1.6"/>
      </svg>
      hello@arlenvoss.com
    </li>
    <li class="contact-item">
      <svg class="contact-icon" viewBox="0 0 32 32" aria-hidden="true">
        <circle cx="16" cy="16" r="16" fill="#1b7aad"/>
        <g fill="none" stroke="#fff" stroke-width="1.4">
          <circle cx="16" cy="16" r="7"/>
          <ellipse cx="16" cy="16" rx="3" ry="7"/>
          <path d="M9 16h14M10 12.5h12M10 19.5h12"/>
        </g>
      </svg>
      www.arlenvoss.com
    </li>
  </ul>
</section>

<section class="card card--back" aria-label="Business card back">
  <div class="edge-tab edge-tab--left"></div>
  <div class="edge-tab edge-tab--right"></div>
  <div class="back-brand">
    <div class="brand-mark"></div>
    <div class="brand-name">Northgate</div>
    <div class="brand-tagline">Consulting Company</div>
  </div>
  <p class="back-email">contact@northgatecyber.com</p>
</section>

</body>
</html>
```